Layout for site fence advertising - length approx. 250 cm x 125 cm

The advertising will later be printed on a PVC film and used for events or on sports fields.

Main services :
Your regional contact at
Real estate and business financing
independent insurance advice

```html
<!DOCTYPE html>
<html lang="en">
<head>
<meta charset="utf-8">
<title>RL Finanzpartner GmbH – Site Fence Banner</title>
<link rel="stylesheet" href="https://fonts.googleapis.com/css2?family=Bebas+Neue&family=Quicksand:wght@600;700&family=Arimo:wght@700&display=swap">
<style>
  :root {
    --brand-blue: #1f4aa0;
    --brand-blue-dark: #17397f;
    --text-grey: #4a4a4a;
    --line-grey: #555555;
    --paper: #ffffff;
    --paper-shade: #eef0f3;
    --stage: #dfe3e8;
    --white: #ffffff;
  }
  * { margin: 0; padding: 0; box-sizing: border-box; }
  html, body {
    width: 1117px; height: 1200px; overflow: hidden;
    background: var(--stage);
  }
  .banner {
    position: absolute; left: 0; top: 320px;
    width: 1117px; height: 560px; overflow: hidden;
    background: linear-gradient(135deg, var(--paper) 0%, var(--paper-shade) 55%, var(--paper) 100%);
  }
  .brand-mark {
    position: absolute; left: 50px; top: 60px;
    width: 124px; height: 124px; border-radius: 50%;
    border: 4px solid var(--brand-blue);
  }
  .brand-divider {
    position: absolute; left: 188px; top: 58px;
    width: 3px; height: 128px; background: var(--line-grey);
  }
  .brand-name {
    position: absolute; left: 200px; top: 100px;
    font-family: "Quicksand", sans-serif; font-weight: 700;
    font-size: 25px; color: var(--brand-blue); white-space: nowrap;
  }
  .brand-tagline {
    position: absolute; left: 200px; top: 134px;
    font-family: "Quicksand", sans-serif; font-weight: 600;
    font-size: 18px; color: var(--text-grey); white-space: nowrap;
  }
  .section-label {
    position: absolute; left: 50px;
    font-family: "Arimo", sans-serif; font-weight: 700;
    font-size: 17px; color: var(--text-grey); white-space: nowrap;
  }
  .section-label.services { top: 240px; }
  .section-label.contact { top: 407px; }
  .services-rule {
    position: absolute; left: 216px; top: 250px;
    width: 446px; height: 2px; background: var(--brand-blue);
  }
  .service-icon { position: absolute; top: 280px; width: 84px; height: 84px; }
  .service-icon.financing { left: 70px; }
  .service-icon.insurance { left: 438px; }
  .service-title {
    position: absolute; top: 288px;
    font-family: "Bebas Neue", sans-serif; font-size: 36px; line-height: 37px;
    letter-spacing: -0.2px;
    color: var(--brand-blue); white-space: nowrap;
  }
  .service-title.financing { left: 168px; }
  .service-title.insurance { left: 537px; }
  .contact-band { position: absolute; left: 0; top: 0; }
  .phone-line {
    position: absolute; left: 50px; top: 456px;
    display: flex; align-items: center; gap: 14px;
    font-family: "Bebas Neue", sans-serif; font-size: 90px; line-height: 90px;
    color: var(--white); white-space: nowrap; letter-spacing: 1px;
  }
  .phone-line svg { width: 52px; height: 52px; }
  .portrait {
    position: absolute; left: 780px; top: 50px;
    width: 337px; height: 510px;
    background: linear-gradient(180deg, #e9d9cf 0%, #c99f8c 40%, #f2f2f2 62%, #1f2436 78%, #1a1f30 100%);
    border-radius: 160px 160px 0 0;
  }
</style>
</head>
<body>
  <main class="banner">
    <div class="brand-mark"></div>
    <div class="brand-divider"></div>
    <div class="brand-name">RL Finanzpartner GmbH</div>
    <div class="brand-tagline">Finanzieren, Versichern, Vorsorgen</div>

    <div class="section-label services">MAIN SERVICES :</div>
    <div class="services-rule"></div>

    <svg class="service-icon financing" viewBox="0 0 88 88" aria-hidden="true">
      <path d="M44 4 A40 40 0 1 0 84 44" fill="none" stroke="var(--brand-blue)" stroke-width="3"/>
      <circle cx="44" cy="44" r="34" fill="var(--brand-blue)"/>
      <path d="M28 44 L44 30 L60 44 M32 41 V56 H56 V41" fill="none" stroke="#fff" stroke-width="2.5" stroke-linejoin="round"/>
      <rect x="40" y="46" width="8" height="10" fill="none" stroke="#fff" stroke-width="2"/>
    </svg>
    <div class="service-title financing">REAL ESTATE AND<br>BUSINESS FINANCING</div>

    <svg class="service-icon insurance" viewBox="0 0 88 88" aria-hidden="true">
      <path d="M44 4 A40 40 0 1 0 84 44" fill="none" stroke="var(--brand-blue)" stroke-width="3"/>
      <circle cx="44" cy="44" r="34" fill="var(--brand-blue)"/>
      <path d="M44 26 L56 31 V41 C56 49 50 54 44 57 C38 54 32 49 32 41 V31 Z" fill="none" stroke="#fff" stroke-width="2.5" stroke-linejoin="round"/>
      <path d="M38 41 L43 46 L51 37" fill="none" stroke="#fff" stroke-width="2.5" stroke-linecap="round" stroke-linejoin="round"/>
    </svg>
    <div class="service-title insurance">INDEPENDENT<br>INSURANCE ADVICE</div>

    <div class="section-label contact">YOUR REGIONAL CONTACT AT</div>

    <svg class="contact-band" width="1117" height="560" aria-hidden="true">
      <polygon points="0,443 368,443 400,410 830,410 830,560 0,560" fill="var(--brand-blue)"/>
    </svg>

    <div class="phone-line">
      <svg viewBox="0 0 24 24" aria-hidden="true">
        <path fill="#fff" d="M6.6 10.8a15.1 15.1 0 0 0 6.6 6.6l2.2-2.2a1 1 0 0 1 1-.25 11.4 11.4 0 0 0 3.6.57 1 1 0 0 1 1 1V20a1 1 0 0 1-1 1A17 17 0 0 1 3 4a1 1 0 0 1 1-1h3.5a1 1 0 0 1 1 1c0 1.25.2 2.45.57 3.570a1 1 0 0 1-.25 1z"/>
      </svg>
      <span>+43 660 555 0142</span>
    </div>

    <div class="portrait" role="img" aria-label="Portrait photo of the regional advisor in a dark suit and white shirt"></div>
  </main>
</body>
</html>
```